Logo+Business Card Design for Architecture Photographer

Hi Everyone,

I am looking for logo/business designs for my new business - Dovel Pictura. My business does commercial photography with a specialization in architecture, luxury real estate, and design. The Int is short for interior and ex is short for exterior.

Some of the values of my business are:
- providing top quality photography and post-processing (straight lines, accurate and bold whites/blacks/colors) for commercial use (websites, social media, advertising campaigns)
- fostering a collaborative workflow that is professional and fun that will have clients returning because of the premium service they received
- asking the right questions so that I can capture what matters to my clients with my own creative vision

I want my final look to be modern and bold. The business cards will be letter pressed/debossed, so the design should incorporate that. I am imagining a solid matte olive green or matte navy blue background on one side and white on the other. The card will be printed on colored cards, so you don't have to put a colored background as part of the design. I have attached some examples of colors I like, although it doesn't matter too much for the purpose of your work.

I want the debossing to be part of the design of the business card. This debossing should be some some of pattern or a frame that holds the logo on the back of the card (I have attached some sample images named geometric debossing to show what I mean). Then I can just foil print my logo on the back. My contact info and a logo will be on the front.

Somewhere it should say "Architecture, Luxury Real Estate, Design".

My vision for the logo: no cameras or buildings. I can't think of anything symbolic for the logo, but it should somehow contain Dovel. It might be cool to have them separated by a line like Do | Vel. Or have the Int inside something, and the Ex outside.

I plan on using Quarvel to print the cards. You can find their specifications here: https://quarvel.example/products/duplex-business-cards?variant=5837204916273

It would be nice to have a psd file that I can edit as well as a PDF to deliver to the printing company. Both must be vector graphics.

Thank you to everyone who has submitted a design as it has helped me get a better idea of what I want.

Target Market(s)

Designers, architects

Industry/Entity Type

Photographer

Contact Information for Business Card

See project description

Logo Text

Dovel Pictura

Font styles to use
Sans Serif
Decorative

Colors
ffffff

Requirements
Must have
• Logo and business card design. Deboss area less than 3 square inches. Deboss area should be some sort of a pattern/design as shown in attachments labelled "Geometric Debossing Example".
• Logo design and deboss design must be submitted in vector graphics.
Nice to have
• Color doesn't have to be shown on the design because I will be printing on colored paper, although it would be helpful to help me visualize what it will eventually look like.
Should not have
• A camera or building in the design...too cliche.

```html
<!DOCTYPE html>
<html lang="en">
<head>
<meta charset="utf-8">
<title>Dovel Pictura — Business Card</title>
<link rel="stylesheet" href="https://fonts.googleapis.com/css2?family=Jost:wght@300;400;500;600&display=swap">
<style>
  :root {
    --backdrop: #d2d2d2;
    --card-white: #ffffff;
    --brand-blue: #0d5aa7;
    --brand-blue-light: #1a7acb;
    --brand-blue-deep: #0a4f98;
    --ink-on-blue: #ffffff;
    --deboss-line: rgba(255, 255, 255, 0.32);
    --deboss-shade: rgba(4, 40, 90, 0.45);
  }
  * { box-sizing: border-box; margin: 0; padding: 0; }
  html, body {
    width: 1200px; height: 900px; overflow: hidden;
    background: var(--backdrop);
    font-family: "Jost", "Futura", sans-serif;
  }
  .sheet {
    width: 1200px; height: 900px;
    display: flex; flex-direction: column; align-items: center; justify-content: center;
    gap: 50px;
  }
  .card {
    position: relative;
    width: 630px; height: 360px;
    box-shadow: 0 6px 18px rgba(0,0,0,0.18);
    overflow: hidden;
  }

  /* Front */
  .card-front { background: var(--card-white); }
  .front-body {
    position: absolute; left: 0; top: 0; right: 0; height: 298px;
    display: flex; align-items: center;
  }
  .front-logo {
    width: 330px; padding-left: 56px; padding-right: 18px;
    color: var(--brand-blue);
    text-align: right;
  }
  .wordmark {
    font-weight: 300; font-size: 42px; letter-spacing: 1px; line-height: 1.05;
    white-space: nowrap;
  }
  .tagline {
    font-weight: 400; font-size: 8.5px; letter-spacing: 1.6px;
    text-transform: uppercase; margin-top: 8px; white-space: nowrap;
  }
  .front-divider {
    width: 1.5px; height: 150px; background: var(--brand-blue);
    margin-top: -30px;
  }
  .contact {
    padding-left: 26px; margin-top: -56px;
    color: var(--brand-blue);
  }
  .contact-name { font-weight: 600; font-size: 17px; letter-spacing: 0.4px; }
  .contact-title { font-weight: 400; font-size: 12.5px; margin-bottom: 16px; }
  .contact-line {
    display: flex; align-items: center; gap: 10px;
    font-size: 12.5px; font-weight: 400; line-height: 1.55;
    white-space: nowrap;
  }
  .contact-line svg { width: 11px; height: 11px; flex: none; }
  .address-band {
    position: absolute; left: 0; right: 0; bottom: 0; height: 62px;
    background: linear-gradient(90deg, var(--brand-blue-deep), var(--brand-blue-light) 35%, var(--brand-blue) 70%, var(--brand-blue-deep));
    display: flex; align-items: center; justify-content: flex-end;
    padding-right: 40px;
  }
  .address {
    color: var(--ink-on-blue); font-size: 13px; font-weight: 400; letter-spacing: 0.5px;
  }

  /* Back */
  .card-back {
    background: linear-gradient(115deg, var(--brand-blue-deep) 0%, var(--brand-blue) 30%, var(--brand-blue-light) 52%, var(--brand-blue) 72%, var(--brand-blue-deep) 100%);
  }
  .deboss-frame {
    position: absolute; left: 115px; top: 70px; width: 400px; height: 220px;
  }
  .back-logo {
    position: absolute; left: 0; right: 0; top: 0; bottom: 0;
    display: flex; flex-direction: column; align-items: center; justify-content: center;
    color: var(--ink-on-blue); text-align: center;
  }
  .back-logo .wordmark { font-size: 50px; }
  .back-logo .tagline { font-size: 10px; letter-spacing: 2.4px; margin-top: 10px; }
</style>
</head>
<body>
  <main class="sheet">
    <section class="card card-front" aria-label="Business card front">
      <div class="front-body">
        <div class="front-logo">
          <div class="wordmark">Dovel Pictura</div>
          <div class="tagline">Architecture, Luxury Real Estate, Design</div>
        </div>
        <div class="front-divider"></div>
        <div class="contact">
          <div class="contact-name">YOUR NAME</div>
          <div class="contact-title">Your Title</div>
          <div class="contact-line">
            <svg viewBox="0 0 12 12" aria-hidden="true"><path fill="currentColor" d="M2.4 0.6 4.3 2.5 3.3 4c.7 1.6 2 2.9 3.6 3.7l1.5-1 1.9 1.9-1.3 1.8C5.2 10.2 1.8 6.8.6 1.9z"/></svg>
            <span>123-456-2100</span>
          </div>
          <div class="contact-line">
            <svg viewBox="0 0 12 12" aria-hidden="true"><rect x="0.5" y="2" width="11" height="8" fill="currentColor"/><path d="M0.8 2.4 6 6.6 11.2 2.4" fill="none" stroke="#fff" stroke-width="1"/></svg>
            <span>youremail@dovelpictura.com</span>
          </div>
          <div class="contact-line">
            <svg viewBox="0 0 12 12" aria-hidden="true"><circle cx="6" cy="6" r="5.5" fill="currentColor"/><g fill="none" stroke="#fff" stroke-width="0.8"><ellipse cx="6" cy="6" rx="2.3" ry="5"/><path d="M1 6h10M1.8 3.5h8.4M1.8 8.5h8.4"/></g></svg>
            <span>www.yourwebsite.com</span>
          </div>
        </div>
      </div>
      <div class="address-band">
        <span class="address">Your address, city, state, ZIP 0000</span>
      </div>
    </section>

    <section class="card card-back" aria-label="Business card back">
      <svg class="deboss-frame" viewBox="0 0 400 220" aria-hidden="true">
        <g fill="none" stroke-width="1.5">
          <g stroke="var(--deboss-shade)" transform="translate(1 1)">
            <rect x="2" y="2" width="396" height="216"/>
            <rect x="14" y="14" width="372" height="192"/>
            <path d="M2 2 14 14M398 2 386 14M2 218 14 206M398 218 386 206"/>
            <path d="M2 60h12M2 160h12M386 60h12M386 160h12M120 2v12M280 2v12M120 206v12M280 206v12"/>
          </g>
          <g stroke="var(--deboss-line)">
            <rect x="2" y="2" width="396" height="216"/>
            <rect x="14" y="14" width="372" height="192"/>
            <path d="M2 2 14 14M398 2 386 14M2 218 14 206M398 218 386 206"/>
            <path d="M2 60h12M2 160h12M386 60h12M386 160h12M120 2v12M280 2v12M120 206v12M280 206v12"/>
          </g>
        </g>
      </svg>
      <div class="back-logo">
        <div class="wordmark">Dovel Pictura</div>
        <div class="tagline">Architecture, Luxury Real Estate, Design</div>
      </div>
    </section>
  </main>
</body>
</html>
```